Supplement Rebranding Bottle Design

READ WORD DOCUMENT ATTACHED.
We want to rebrand our current health supplements (see below). We do want it to be modern, vibrant and appealing. Very upscale and elegant as it targets primarily women.
Bottle size: see pictures for bottle size, along with sample bottles that we like; we’re open to any bottle similar to the ones attached.
Current bottles: So ideally, we’d keep the core color on each bottle with a new branding/bottle design. But we're open to your suggestion.

Target Market(s)

mostly women but shouldn't be overly feminine

Requirements
Must have
• see bottle sizes attached

```html
<!DOCTYPE html>
<html lang="en">
<head>
<meta charset="utf-8">
<title>Vela Supplement Labels</title>
<link href="https://fonts.googleapis.com/css2?family=Archivo+Black&family=Archivo:wght@700;800&display=swap" rel="stylesheet">
<style>
  :root {
    --page: #ffffff;
    --label-bg: #f9f9f9;
    --ink: #111111;
    --heading: #333333;
    --copy: #2e2e2e;
    --liver: #edd7f2;
    --tummy: #ff7f7f;
    --hormone: #abdf87;
    --sugar: #89ccdd;
  }
  * { margin: 0; padding: 0; box-sizing: border-box; }
  html, body {
    width: 1200px; height: 1200px; overflow: hidden;
    background: var(--page);
  }
  .sheet {
    position: relative;
    width: 1125px; height: 1125px;
    transform: scale(1.06667);
    transform-origin: 0 0;
  }
  .label {
    position: absolute;
    width: 454px; height: 514px;
    background: var(--label-bg);
  }
  .label--liver   { left: 71px;  top: 38px;  --accent: var(--liver); }
  .label--tummy   { left: 600px; top: 38px;  --accent: var(--tummy); }
  .label--hormone { left: 71px;  top: 573px; --accent: var(--hormone); }
  .label--sugar   { left: 600px; top: 573px; --accent: var(--sugar); }

  .label__art { position: absolute; inset: 0; width: 454px; height: 514px; }
  .label__art .accent { fill: var(--accent); }
  .label__art .frame {
    fill: none; stroke: var(--ink); stroke-width: 3; stroke-linejoin: miter;
  }

  .label__brand {
    position: absolute; left: 186px; top: 38px;
    font-family: "Archivo Black", sans-serif;
    font-size: 40px; line-height: 1; color: var(--ink);
    letter-spacing: 1px;
  }
  .label__name {
    position: absolute; left: 74px; top: 137px;
    font-family: "Archivo Black", sans-serif;
    font-size: 31px; line-height: 1; color: var(--heading);
    white-space: nowrap;
  }
  .label__facts {
    position: absolute; left: 74px; top: 191px;
    list-style: none;
    font-family: "Archivo", sans-serif; font-weight: 800;
    font-size: 13.5px; line-height: 20.5px; color: var(--copy);
    letter-spacing: 0.3px; white-space: nowrap;
  }
</style>
</head>
<body>
<main class="sheet">

  <section class="label label--liver">
    <svg class="label__art" viewBox="0 0 454 514" aria-hidden="true">
      <rect class="accent" x="293" y="3" width="161" height="24"/>
      <path class="accent" d="M48 89 H169 V370 H363 V465 H48 Z"/>
      <polyline class="frame" points="169,34 24,34 24,490 434,485 434,73 374,71"/>
    </svg>
    <div class="label__brand">Vela</div>
    <h2 class="label__name">Liver Vela</h2>
    <ul class="label__facts">
      <li>Rejuvenating Cleanse &amp; Detox Formula*</li>
      <li>Dietary Supplement</li>
      <li>120 Vegetable Capsules</li>
    </ul>
  </section>

  <section class="label label--tummy">
    <svg class="label__art" viewBox="0 0 454 514" aria-hidden="true">
      <rect class="accent" x="293" y="3" width="161" height="24"/>
      <path class="accent" d="M45 89 H413 V185 H289 V465 H168 V185 H45 Z"/>
      <polyline class="frame" points="169,34 24,34 24,490 434,485 434,73 374,71"/>
    </svg>
    <div class="label__brand">Vela</div>
    <h2 class="label__name">Tummy Vela</h2>
    <ul class="label__facts">
      <li>Oxygenating Colon Cleanse*</li>
      <li>Dietary Supplement</li>
      <li>90 Vegetable Capsules</li>
    </ul>
  </section>

  <section class="label label--hormone">
    <svg class="label__art" viewBox="0 0 454 514" aria-hidden="true">
      <rect class="accent" x="293" y="3" width="161" height="24"/>
      <path class="accent" d="M41 88 H162 V227 H296 V88 H416 V464 H296 V322 H162 V464 H41 Z"/>
      <polyline class="frame" points="169,34 24,34 24,490 434,485 434,73 374,71"/>
    </svg>
    <div class="label__brand">Vela</div>
    <h2 class="label__name">Hormone Vela</h2>
    <ul class="label__facts">
      <li>Rejuvenating Cleanse &amp; Detox Formula*</li>
      <li>Dietary Supplement</li>
      <li>120 Vegetable Capsules</li>
    </ul>
  </section>

  <section class="label label--sugar">
    <svg class="label__art" viewBox="0 0 454 514" aria-hidden="true">
      <rect class="accent" x="293" y="3" width="161" height="24"/>
      <path class="accent" fill-rule="evenodd" d="M50 88 H290 C370 88 405 130 405 185 C405 230 385 258 342 270 C392 282 413 318 413 360 C413 430 370 464 290 464 H50 Z
        M170 164 H262 C280 164 290 180 290 200 C290 222 280 235 262 235 H170 Z
        M170 312 H265 C282 312 290 325 290 345 C290 365 282 377 265 377 H170 Z"/>
      <polyline class="frame" points="169,34 24,34 24,490 434,485 434,73 374,71"/>
    </svg>
    <div class="label__brand">Vela</div>
    <h2 class="label__name">Blood Sugar Vela</h2>
    <ul class="label__facts">
      <li>Supports Healthy Blood Glucose Levels*</li>
      <li>Dietary Supplement</li>
      <li>Dietary Supplement</li>
    </ul>
  </section>

</main>
</body>
</html>
```